VELOXA SPORTS NETWORK

design a website that will be a companion to a sports network that features womens sports and fitness content.
With the goal of promoting and empowering female athleticism, Veloxatv.example will be the online network that connects female sports fans to the sports they love and follow. The site aims to raise the level of awareness of women in sports by providing comprehensive sports coverage, spotlighting outstanding achievements, and working with sporting associations on advocacy issues and empowering programs.
Updates
I would like to have all entry by Sunday June 8 2014 thank you
please use actual script not lorem ipsum
thank you
Deadline winding down, added new pictures to file
Target Market(s)
our target market is females 18-54, whom love womens sports and ftiness
Industry/Entity Type
Fitness
Requirements
Must have
- Attributes of the website:
1. Large Photos: to accompany current stories
2. Colorful: Highlight Veloxa’s officials colors
3. News Area: recent news items on the home page and achieved news stories
4. Featured Content area: Headline news, athlete spotlights and issues
5. Streaming content: to accompany news and featured content
6. Advertiser links: to purchase merchandise
7. Real-time scores of live events
8. Blog
9. Monthly newsletter
10. Athlete profile page
11. Model close to QRVT
Nice to have
- Veloxatv.example will offer value-added service that will entitle customers to gain access to online streaming services provided by Veloxa, which delivers both live streams and on-demand replays of global women’s sports events to sports fans in U.S. and abroad. This service will be subscription based for a modest monthly fee. Content will be available across multiple platforms and cloud based. New subscriber will get first 30 days free.
Content will include:
1. Live sports events
2. On-demand and premium content
3. Fan-generated Content

```html
<!DOCTYPE html>
<html lang="en">
<head>
<meta charset="utf-8">
<title>Veloxa Sports Network</title>
<link href="https://fonts.googleapis.com/css2?family=Open+Sans:wght@400;600;700&family=Roboto+Condensed:wght@400;700&display=swap" rel="stylesheet">
<style>
:root{
  --red:#e4202a;
  --red-dark:#b8141c;
  --red-soft:#f25a4a;
  --ink:#333;
  --muted:#777;
  --line:#e2e2e2;
  --page:#ffffff;
  --panel:#f4f4f4;
  --dark:#2b2b2b;
}
*{box-sizing:border-box;margin:0;padding:0}
html,body{width:1200px;height:2312px;overflow:hidden;background:var(--page);font-family:"Open Sans",Arial,sans-serif;color:var(--ink)}
.canvas{position:relative;width:1200px;height:2312px;overflow:hidden}
.abs{position:absolute}

/* nav */
.topnav{left:0;top:0;width:1200px;height:44px;background:var(--red);display:flex;align-items:center;padding:0 28px;color:#fff}
.brand{display:flex;align-items:center;gap:8px;font-family:"Roboto Condensed",sans-serif;font-weight:700;font-size:22px;letter-spacing:1px;color:#fff}
.brand .dot{width:14px;height:14px;border-radius:50%;background:#fff}
.menu{display:flex;gap:16px;margin-left:60px;font-size:11px;font-weight:600}
.menu span.on{background:var(--red-dark);padding:4px 10px;border-radius:2px}
.search{margin-left:auto;width:150px;height:22px;background:#fff;border-radius:2px}

/* hero */
.hero{left:0;top:44px;width:1200px;height:326px;background:
  radial-gradient(ellipse 380px 260px at 300px 170px,#b9a89b 0%,rgba(185,168,155,0) 70%),
  linear-gradient(90deg,#4a4d51 0%,#7c7f83 35%,#b4b6b8 60%,#d8d9da 80%,#c3c4c6 100%)}
.hero-copy{left:640px;top:150px;width:440px;display:flex;flex-direction:column;align-items:center}
.hero-name{display:flex;align-items:center;gap:12px;font-family:"Roboto Condensed",sans-serif;font-weight:700;font-size:48px;line-height:1;color:var(--red);letter-spacing:2px}
.hero-name i{width:22px;height:22px;border-radius:50%;background:var(--red)}
.hero-sub{margin-top:6px;font-size:10px;font-weight:700;color:#fff;letter-spacing:3px}
.hero-tag{margin-top:8px;font-family:"Roboto Condensed",sans-serif;font-weight:700;font-size:15px;color:var(--red);text-transform:uppercase;white-space:nowrap}
.hero-btns{margin-top:16px;display:flex;gap:14px}
.btn{background:var(--red);color:#fff;font-weight:700;font-size:13px;padding:8px 18px;border-radius:3px;border:2px solid #fff;white-space:nowrap}

/* ticker */
.ticker{left:0;top:372px;width:1200px;height:28px;background:var(--red);display:flex;align-items:center;gap:26px;padding-left:180px;color:#fff;font-size:12px;font-weight:700}
.ticker span::before{content:"";display:inline-block;width:6px;height:6px;background:#fff;transform:rotate(45deg);margin-right:8px;vertical-align:middle}

/* media */
.play{position:absolute;width:34px;height:34px;left:50%;top:50%;margin:-17px 0 0 -17px}

.feature{left:180px;top:412px;width:540px;height:388px;background:linear-gradient(160deg,#7fb7d9 0%,#d7c9a8 55%,#8c7b62 100%)}
.feature .play{width:60px;height:60px;margin:-30px 0 0 -30px}

.promo{left:732px;top:412px;width:288px;height:148px;background:linear-gradient(135deg,var(--red) 0%,var(--red-dark) 100%);padding:16px;color:#fff}
.promo h2{font-family:"Roboto Condensed",sans-serif;font-size:22px;line-height:1.1;font-weight:700;width:190px}
.promo .click{display:inline-block;margin-top:10px;background:#fff;color:var(--red);font-size:11px;font-weight:700;padding:4px 10px;border-radius:2px}
.promo .badge{position:absolute;right:14px;top:36px;width:64px;height:64px;border-radius:50%;background:#fff}
.register{left:732px;top:566px;width:288px;height:30px;background:var(--red-soft);color:#fff;font-weight:700;font-size:13px;display:flex;align-items:center;padding-left:14px}
.ready{left:732px;top:604px;width:288px;height:336px;background:linear-gradient(180deg,#c9c9c9 0%,#ececec 100%)}
.ready p{position:absolute;right:16px;top:90px;width:150px;text-align:right;font-family:"Roboto Condensed",sans-serif;font-weight:700;font-size:24px;line-height:1.1;color:var(--red);text-transform:uppercase}

/* tiles */
.tiles{left:180px;top:808px;width:540px;display:grid;grid-template-columns:repeat(3,174px);grid-auto-rows:232px;gap:8px 9px}
.tile{position:relative;background:#ddd}
.tile .img{position:absolute;left:0;top:0;width:174px;height:186px}
.tile .cap{position:absolute;left:0;bottom:0;width:174px;height:46px;background:var(--red);color:#fff;padding:6px 8px}
.tile .cap b{display:block;font-family:"Roboto Condensed",sans-serif;font-size:13px}
.tile .cap i{font-style:normal;font-size:9px;opacity:.9}
.tile.all{background:linear-gradient(135deg,var(--red) 0%,var(--red-dark) 100%);color:#fff;display:flex;flex-direction:column;justify-content:center;padding:16px}
.tile.all small{font-size:11px;font-weight:700}
.tile.all strong{font-family:"Roboto Condensed",sans-serif;font-size:26px;line-height:1.05}
.g1{background:linear-gradient(135deg,#d97f5c,#f1c6a5)}
.g2{background:linear-gradient(135deg,#c94a3b,#efb8a0)}
.g3{background:linear-gradient(135deg,#b8a896,#ece2d4)}
.g4{background:linear-gradient(135deg,#9d2f2a,#e98b70)}
.g5{background:linear-gradient(135deg,#6f8fb3,#d9d2c4)}
.g6{background:linear-gradient(135deg,#cc6d55,#f3d1bb)}

/* side panels */
.sec-title{font-family:"Roboto Condensed",sans-serif;font-weight:700;font-size:15px;color:var(--red);text-transform:uppercase;border-bottom:2px solid var(--red);padding-bottom:4px;margin-bottom:8px}
.headlines{left:732px;top:950px;width:288px}
.headlines li{list-style:none;font-size:10px;line-height:17px;padding-left:12px;position:relative;color:var(--ink)}
.headlines li::before{content:"";position:absolute;left:0;top:6px;width:5px;height:5px;background:var(--red)}
.more{font-size:10px;font-weight:700;color:var(--red);margin-top:6px}

.spot{left:732px;top:1210px;width:288px}
.spot-grid{display:grid;grid-template-columns:repeat(3,92px);grid-auto-rows:88px;gap:6px}
.spot-grid div{position:relative}
.spot-grid .play{width:24px;height:24px;margin:-12px 0 0 -12px}

.topc{left:732px;top:1550px;width:288px}
.topc .item{display:flex;gap:10px;margin-bottom:12px}
.topc .ico{width:30px;height:30px;background:var(--red);flex:none;display:flex;align-items:center;justify-content:center}
.topc p{font-size:10px;line-height:14px}
.topc p b{color:var(--dark)}

.shop{left:732px;top:1810px;width:288px}
.shop .head{display:flex;justify-content:space-between;align-items:center}
.shop .now{background:var(--panel);border:1px solid var(--line);font-size:10px;padding:3px 8px}
.shop .img{width:288px;height:120px;background:linear-gradient(180deg,#f0f0f0,#d6d6d6);margin:8px 0}
.shop li{list-style:none;display:flex;justify-content:space-between;font-size:10px;line-height:17px;border-bottom:1px dotted var(--line)}

.events{left:180px;top:1776px;width:540px}
.events .ev{border-bottom:1px solid var(--line);padding:6px 0}
.events .date{font-size:9px;color:var(--red);font-weight:700}
.events h4{font-size:11px;font-weight:700;color:var(--dark)}
.events p{font-size:9px;line-height:13px;color:var(--muted)}

.partners{left:180px;top:2100px;width:840px;height:56px;display:flex;justify-content:space-around;align-items:center;border-top:1px solid var(--line);border-bottom:1px solid var(--line)}
.partners div{width:90px;height:26px;background:#d0d0d0}

.footer{left:180px;top:2176px;width:840px;height:120px;border-top:3px solid var(--red);padding-top:14px;display:flex;justify-content:space-between;align-items:flex-start}
.social{display:flex;gap:8px}
.social span{width:26px;height:26px;border-radius:50%;background:#9aa3ad}
.foot-text{width:440px;font-size:9px;line-height:13px;color:var(--muted);text-align:right}
.foot-brand{display:flex;align-items:center;gap:6px;font-family:"Roboto Condensed",sans-serif;font-weight:700;font-size:16px;color:var(--red)}
.foot-brand i{width:12px;height:12px;border-radius:50%;background:var(--red)}
</style>
</head>
<body>
<div class="canvas">

  <header class="abs topnav">
    <div class="brand"><span class="dot"></span>VELOXA</div>
    <nav class="menu">
      <span class="on">Home</span><span>Sports</span><span>Columns</span><span>Video</span><span>Reviews</span><span>Newsletter</span><span>Blog</span><span>Shop</span><span>TV</span><span>Forum</span><span>Athletes</span><span>Sign In</span><span>Register</span>
    </nav>
    <div class="search"></div>
  </header>

  <section class="abs hero" role="img" aria-label="Female athlete holding a plank on a bench in a bright gym"></section>
  <div class="abs hero-copy">
    <div class="hero-name"><i></i>VELOXA</div>
    <div class="hero-sub">SPORTS NETWORK</div>
    <div class="hero-tag">Empowering athletes in a state of motion</div>
    <div class="hero-btns"><span class="btn">Start Free Trial</span><span class="btn">Get Registered Now!</span></div>
  </div>

  <div class="abs ticker">
    <span>Live score ticker tape</span><span>Live score ticker tape</span><span>Live score ticker tape</span><span>Live score ticker tape</span><span>Live score ticker tape</span>
  </div>

  <div class="abs feature" role="img" aria-label="Featured video still of a stadium event">
    <svg class="play" viewBox="0 0 60 60"><circle cx="30" cy="30" r="28" fill="rgba(228,32,42,.9)"/><path d="M24 18 L42 30 L24 42Z" fill="#fff"/></svg>
  </div>

  <div class="abs promo">
    <h2>NEW SUBSCRIBER WILL GET FIRST 30 DAY'S FREE</h2>
    <span class="click">Click Here !</span>
    <span class="badge"></span>
  </div>
  <div class="abs register">Get Registered Now!</div>
  <div class="abs ready" role="img" aria-label="Athlete stretching on a court">
    <p>Get ready for unlimited live sport events</p>
  </div>

  <div class="abs tiles">
    <div class="tile"><div class="img g1" role="img" aria-label="Sprinter on the track"><svg class="play" viewBox="0 0 34 34"><circle cx="17" cy="17" r="16" fill="rgba(228,32,42,.9)"/><path d="M13 10 L24 17 L13 24Z" fill="#fff"/></svg></div><div class="cap"><b>RUNNING MIRACLE</b><i>Comeback on the final lap</i></div></div>
    <div class="tile"><div class="img g2" role="img" aria-label="Team celebrating on the field"><svg class="play" viewBox="0 0 34 34"><circle cx="17" cy="17" r="16" fill="rgba(228,32,42,.9)"/><path d="M13 10 L24 17 L13 24Z" fill="#fff"/></svg></div><div class="cap"><b>SOCCER NIGHTS</b><i>Highlights from the weekend</i></div></div>
    <div class="tile"><div class="img g3" role="img" aria-label="Hurdler mid jump"><svg class="play" viewBox="0 0 34 34"><circle cx="17" cy="17" r="16" fill="rgba(228,32,42,.9)"/><path d="M13 10 L24 17 L13 24Z" fill="#fff"/></svg></div><div class="cap"><b>HURDLE HEROES</b><i>Record set in the final</i></div></div>
    <div class="tile"><div class="img g4" role="img" aria-label="Volleyball players at the net"><svg class="play" viewBox="0 0 34 34"><circle cx="17" cy="17" r="16" fill="rgba(228,32,42,.9)"/><path d="M13 10 L24 17 L13 24Z" fill="#fff"/></svg></div><div class="cap"><b>NET GAINS</b><i>Volleyball season preview</i></div></div>
    <div class="tile"><div class="img g6" role="img" aria-label="Tennis player serving"><svg class="play" viewBox="0 0 34 34"><circle cx="17" cy="17" r="16" fill="rgba(228,32,42,.9)"/><path d="M13 10 L24 17 L13 24Z" fill="#fff"/></svg></div><div class="cap"><b>CENTER COURT</b><i>Open round two recap</i></div></div>
    <div class="tile"><div class="img g5" role="img" aria-label="Swimmer at the pool"><svg class="play" viewBox="0 0 34 34"><circle cx="17" cy="17" r="16" fill="rgba(228,32,42,.9)"/><path d="M13 10 L24 17 L13 24Z" fill="#fff"/></svg></div><div class="cap"><b>POOL POWER</b><i>Relay team takes gold</i></div></div>
    <div class="tile"><div class="img g2" role="img" aria-label="Fitness class in a studio"><svg class="play" viewBox="0 0 34 34"><circle cx="17" cy="17" r="16" fill="rgba(228,32,42,.9)"/><path d="M13 10 L24 17 L13 24Z" fill="#fff"/></svg></div><div class="cap"><b>FIT IN TEN</b><i>Quick core workout</i></div></div>
    <div class="tile"><div class="img g3" role="img" aria-label="Basketball player driving to the hoop"><svg class="play" viewBox="0 0 34 34"><circle cx="17" cy="17" r="16" fill="rgba(228,32,42,.9)"/><path d="M13 10 L24 17 L13 24Z" fill="#fff"/></svg></div><div class="cap"><b>HOOP DREAMS</b><i>Rookie of the month</i></div></div>
    <div class="tile"><div class="img g1" role="img" aria-label="Gymnast on the beam"><svg class="play" viewBox="0 0 34 34"><circle cx="17" cy="17" r="16" fill="rgba(228,32,42,.9)"/><path d="M13 10 L24 17 L13 24Z" fill="#fff"/></svg></div><div class="cap"><b>BALANCE BEAM</b><i>Perfect ten routine</i></div></div>
    <div class="tile"><div class="img g5" role="img" aria-label="Cyclist on a mountain road"><svg class="play" viewBox="0 0 34 34"><circle cx="17" cy="17" r="16" fill="rgba(228,32,42,.9)"/><path d="M13 10 L24 17 L13 24Z" fill="#fff"/></svg></div><div class="cap"><b>HILL CLIMB</b><i>Stage five in review</i></div></div>
    <div class="tile"><div class="img g4" role="img" aria-label="Boxer training on a bag"><svg class="play" viewBox="0 0 34 34"><circle cx="17" cy="17" r="16" fill="rgba(228,32,42,.9)"/><path d="M13 10 L24 17 L13 24Z" fill="#fff"/></svg></div><div class="cap"><b>RING READY</b><i>Title fight build up</i></div></div>
    <div class="tile all"><small>MORE VIDEOS</small><strong>CLICK HERE TO VIEW ALL</strong></div>
  </div>

  <section class="abs headlines">
    <div class="sec-title">Headline News</div>
    <ul>
      <li>National team clinches spot in world final</li>
      <li>Record crowd fills arena for league opener</li>
      <li>Rookie guard named player of the week</li>
      <li>Marathon champion returns from injury</li>
      <li>New league season schedule announced today</li>
      <li>Swimmers break relay mark at trials</li>
      <li>Coach signs extension through next season</li>
      <li>Tennis star advances to quarterfinals</li>
      <li>Youth program expands to ten new cities</li>
      <li>Softball team wins conference title</li>
      <li>Cyclist takes lead after mountain stage</li>
    </ul>
    <div class="more">More Headlines</div>
  </section>

  <section class="abs spot">
    <div class="sec-title">Athlete Spotlights</div>
    <div class="spot-grid">
      <div class="g1" role="img" aria-label="Athlete portrait"><svg class="play" viewBox="0 0 34 34"><circle cx="17" cy="17" r="16" fill="rgba(228,32,42,.9)"/><path d="M13 10 L24 17 L13 24Z" fill="#fff"/></svg></div>
      <div class="g3" role="img" aria-label="Athlete portrait"><svg class="play" viewBox="0 0 34 34"><circle cx="17" cy="17" r="16" fill="rgba(228,32,42,.9)"/><path d="M13 10 L24 17 L13 24Z" fill="#fff"/></svg></div>
      <div class="g6" role="img" aria-label="Athlete portrait"><svg class="play" viewBox="0 0 34 34"><circle cx="17" cy="17" r="16" fill="rgba(228,32,42,.9)"/><path d="M13 10 L24 17 L13 24Z" fill="#fff"/></svg></div>
      <div class="g2" role="img" aria-label="Athlete portrait"><svg class="play" viewBox="0 0 34 34"><circle cx="17" cy="17" r="16" fill="rgba(228,32,42,.9)"/><path d="M13 10 L24 17 L13 24Z" fill="#fff"/></svg></div>
      <div class="g5" role="img" aria-label="Athlete portrait"><svg class="play" viewBox="0 0 34 34"><circle cx="17" cy="17" r="16" fill="rgba(228,32,42,.9)"/><path d="M13 10 L24 17 L13 24Z" fill="#fff"/></svg></div>
      <div class="g1" role="img" aria-label="Athlete portrait"><svg class="play" viewBox="0 0 34 34"><circle cx="17" cy="17" r="16" fill="rgba(228,32,42,.9)"/><path d="M13 10 L24 17 L13 24Z" fill="#fff"/></svg></div>
      <div class="g4" role="img" aria-label="Athlete portrait"><svg class="play" viewBox="0 0 34 34"><circle cx="17" cy="17" r="16" fill="rgba(228,32,42,.9)"/><path d="M13 10 L24 17 L13 24Z" fill="#fff"/></svg></div>
      <div class="g6" role="img" aria-label="Athlete portrait"><svg class="play" viewBox="0 0 34 34"><circle cx="17" cy="17" r="16" fill="rgba(228,32,42,.9)"/><path d="M13 10 L24 17 L13 24Z" fill="#fff"/></svg></div>
      <div class="g3" role="img" aria-label="Athlete portrait"><svg class="play" viewBox="0 0 34 34"><circle cx="17" cy="17" r="16" fill="rgba(228,32,42,.9)"/><path d="M13 10 L24 17 L13 24Z" fill="#fff"/></svg></div>
    </div>
  </section>

  <section class="abs topc">
    <div class="sec-title">Top Content</div>
    <div class="item"><span class="ico"><svg width="14" height="14" viewBox="0 0 14 14"><path d="M3 2 L12 7 L3 12Z" fill="#fff"/></svg></span><p><b>Five drills that build sprint speed fast</b><br>Coaches share simple routines for every level.</p></div>
    <div class="item"><span class="ico"><svg width="14" height="14" viewBox="0 0 14 14"><path d="M3 2 L12 7 L3 12Z" fill="#fff"/></svg></span><p><b>Inside the locker room before the final</b><br>An exclusive look at game day rituals.</p></div>
    <div class="item"><span class="ico"><svg width="14" height="14" viewBox="0 0 14 14"><path d="M3 2 L12 7 L3 12Z" fill="#fff"/></svg></span><p><b>Why equal coverage matters for fans</b><br>Our columnists weigh in on the season.</p></div>
    <div class="item"><span class="ico"><svg width="14" height="14" viewBox="0 0 14 14"><path d="M3 2 L12 7 L3 12Z" fill="#fff"/></svg></span><p><b>Recovery tips from pro athletes</b><br>Sleep, fuel and rest days explained.</p></div>
  </section>

  <section class="abs shop">
    <div class="head"><div class="sec-title" style="flex:1">Veloxa Shop</div><span class="now">Shop Now</span></div>
    <div class="img" role="img" aria-label="Woman exercising with training equipment"></div>
    <ul>
      <li><span>Top Quality Equipments</span><span>$99.00</span></li>
      <li><span>Top Quality Clothing</span><span>$49.00</span></li>
      <li><span>Top Quality Footwear</span><span>$79.00</span></li>
      <li><span>Top Quality Equipments</span><span>$99.00</span></li>
    </ul>
  </section>

  <section class="abs events">
    <div class="sec-title">Global Women's Sports Events</div>
    <div class="ev"><div class="date">May 3, 2014 | 6:30 pm</div><h4>VIDEO: It's getting late in Cleveland</h4><p>Late goal seals the series win as the home side rallies in front of a packed and loud crowd.</p></div>
    <div class="ev"><div class="date">May 5, 2014 | 7:00 pm</div><h4>VIDEO: Relay team storms to gold</h4><p>The anchor leg made up two seconds to bring home the title at the spring championships.</p></div>
    <div class="ev"><div class="date">May 8, 2014 | 5:15 pm</div><h4>VIDEO: Open draw set for next week</h4><p>Top seeds learn their paths as the tournament prepares for its biggest field in years.</p></div>
    <div class="ev"><div class="date">May 12, 2014 | 8:00 pm</div><h4>VIDEO: Rookies shine in league debut</h4><p>Three first year players post double figures in a thrilling overtime opener on the road.</p></div>
  </section>

  <div class="abs partners"><div></div><div></div><div></div><div></div></div>

  <footer class="abs footer">
    <div class="social"><span></span><span></span><span></span><span></span><span></span><span></span></div>
    <div class="foot-text">About Veloxa · Advertise · Newsletter · Careers · Contact Us · Privacy Policy · Terms of Use<br>© 2014 Veloxa Sports Network. All rights reserved. Live scores and streams for fans.</div>
    <div class="foot-brand"><i></i>VELOXA</div>
  </footer>

</div>
</body>
</html>
```